Knockdown rebuild flyer - SIZE DL

Wanting a brochure with similar layout attached with images provided.
Left hand side
REBUILD WITH TALLOWAY

Running down the page
step 1: Design
design your dream home.
step 2: Select
personalise your new home
step 3:Demolish
it's in the title
step 4:Build
watch your dream take shape
step 5:Live
move into your new dream home and build new memories

bottom left
Contact: Tom Varde- 0452716038 -Tom@tallowaybuild.com.au

house image similar to the attached example, Tbc logo top right corner.

Target Market(s)

knockdown rebuild clients

Industry/Entity Type

new home building

Font styles to use
Other font styles liked:
• melbourne

Requirements
Nice to have
• attached image

```html
<!DOCTYPE html>
<html lang="en">
<head>
<meta charset="utf-8">
<title>Rebuild with Talloway – DL Flyer</title>
<link href="https://fonts.googleapis.com/css2?family=Arimo:wght@400;500&family=Kalam:wght@400&display=swap" rel="stylesheet">
<style>
  :root {
    --page-bg: #d6d6d6;
    --navy-deep: #0a1838;
    --navy-mid: #163a72;
    --white: #ffffff;
    --ink: #0d1526;
    --photo-fill: #8fa6b8;
    --photo-edge: #8fb0dc;
  }
  html, body {
    margin: 0;
    width: 1200px;
    height: 1200px;
    overflow: hidden;
    background: var(--page-bg);
  }
  .flyer {
    position: absolute;
    left: 50px;
    top: 341px;
    width: 1100px;
    height: 519px;
    display: block;
  }
  .flyer-title {
    font-family: "Kalam", cursive;
    font-size: 49px;
    letter-spacing: 2px;
    fill: var(--white);
  }
  .step-text {
    font-family: "Arimo", Arial, sans-serif;
    font-size: 28px;
    fill: var(--white);
  }
  .contact-phone {
    font-family: "Arimo", Arial, sans-serif;
    font-weight: 500;
    font-size: 35px;
    fill: var(--white);
  }
  .contact-email {
    font-family: "Arimo", Arial, sans-serif;
    font-weight: 500;
    font-size: 36px;
    fill: var(--ink);
  }
  .step-ring {
    fill: var(--navy-deep);
    stroke: var(--white);
    stroke-width: 4;
  }
  .step-link {
    stroke: var(--white);
    stroke-width: 3;
  }
  .step-icon {
    fill: none;
    stroke: var(--white);
    stroke-width: 2;
    stroke-linejoin: round;
  }
</style>
</head>
<body>
<svg class="flyer" viewBox="0 0 1593 751" xmlns="http://www.w3.org/2000/svg">
  <defs>
    <radialGradient id="navy-glow" cx="0.35" cy="0.5" r="0.7">
      <stop offset="0" stop-color="var(--navy-mid)"/>
      <stop offset="1" stop-color="var(--navy-deep)"/>
    </radialGradient>
  </defs>

  <!-- navy panel -->
  <rect class="navy-panel" x="0" y="0" width="1593" height="751" fill="url(#navy-glow)"/>

  <!-- house photo area -->
  <polygon class="photo-band" points="883,0 905,0 845,751 822,751" fill="var(--photo-edge)" opacity="0.45"/>
  <polygon class="house-photo" role="img" aria-label="Photo of a modern single-storey white home with grey tiled roof, lawn and garden pond under a blue sky"
           points="905,0 1593,0 1593,751 865,751 792,359" fill="var(--photo-fill)"/>

  <!-- title -->
  <rect class="title-marker" x="0" y="39" width="42" height="65" fill="var(--white)"/>
  <text class="flyer-title" x="60" y="90">Rebuild with Talloway</text>

  <!-- left step column -->
  <line class="step-link" x1="103" y1="236" x2="103" y2="293"/>
  <line class="step-link" x1="103" y1="369" x2="103" y2="429"/>
  <circle class="step-ring" cx="103" cy="198" r="38"/>
  <circle class="step-ring" cx="103" cy="331" r="38"/>
  <circle class="step-ring" cx="103" cy="467" r="38"/>

  <g class="step-icon">
    <path d="M86 196 L103 182 L120 196 M89 194 V212 H117 V194 M95 212 V202 H101 V212 M106 200 H113 V206 H106 Z"/>
    <path d="M90 315 H114 V348 H90 Z M94 315 V348 M99 331 L104 326 L109 331 M100 331 V336 H108 V331 M117 318 V346"/>
    <path d="M88 470 H118 V486 H88 Z M88 478 H118 M96 470 V478 M110 470 V478 M103 478 V486 M103 448 V456 M103 466 m-6 0 a6 6 0 1 0 12 0 a6 6 0 1 0 -12 0"/>
  </g>

  <text class="step-text" x="175" y="184">Design design</text>
  <text class="step-text" x="175" y="216">your dream</text>
  <text class="step-text" x="175" y="249">home.</text>

  <text class="step-text" x="174" y="313">Select</text>
  <text class="step-text" x="174" y="345">ersonalise</text>
  <text class="step-text" x="174" y="377">your new home</text>

  <text class="step-text" x="174" y="455">Demolish</text>
  <text class="step-text" x="174" y="487">it's in the title</text>

  <!-- right step column -->
  <line class="step-link" x1="451" y1="236" x2="451" y2="293"/>
  <circle class="step-ring" cx="451" cy="198" r="38"/>
  <circle class="step-ring" cx="451" cy="331" r="38"/>

  <g class="step-icon">
    <path d="M434 214 L450 196 M446 192 L456 182 L462 188 L452 198 Z M454 200 L466 212 M458 204 V212 H466"/>
    <path d="M434 330 L451 314 L468 330 M438 327 V348 H464 V327 M443 348 V336 H449 V348 M453 336 H461 V344 H453 Z M451 323 m-3 0 a3 3 0 1 0 6 0 a3 3 0 1 0 -6 0"/>
  </g>

  <text class="step-text" x="526" y="184">Build watch your</text>
  <text class="step-text" x="526" y="216">dream take</text>
  <text class="step-text" x="526" y="249">shape</text>

  <text class="step-text" x="525" y="313">Live move into</text>
  <text class="step-text" x="525" y="345">your new dream</text>
  <text class="step-text" x="525" y="377">home and build</text>
  <text class="step-text" x="525" y="409">new memories.</text>

  <!-- phone contact -->
  <rect class="phone-badge" x="60" y="582" width="40" height="42" rx="6" fill="var(--white)"/>
  <path class="phone-glyph" d="M73 590 q-5 3 -2 14 q4 11 12 13 l4 -5 l-5 -5 l-3 2 q-3 -3 -4 -8 l3 -2 l-1 -8 z" fill="var(--navy-deep)"/>
  <text class="contact-phone" x="136" y="620">Tom Varde- 0452716038</text>

  <!-- email band -->
  <polygon class="email-band" points="0,659 620,659 672,751 0,751" fill="var(--white)"/>
  <g class="envelope-icon">
    <rect x="61" y="689" width="52" height="28" fill="var(--ink)"/>
    <path d="M61 689 L87 706 L113 689 M61 717 L81 702 M113 717 L93 702" fill="none" stroke="var(--white)" stroke-width="2.5"/>
  </g>
  <text class="contact-email" x="134" y="716">Tom@tallowaybuild.com.au</text>
</svg>
</body>
</html>
```